Korvex Systems*

Stationary design including business cards, letter heads, envelops and email signatures using our new logo

Target Market(s)

Innovative Technologies

Industry/Entity Type

Defense Contracting

Font styles to use
Sans Serif

```html
<!DOCTYPE html>
<html lang="en">
<head>
<meta charset="utf-8">
<title>Korvex Systems – Business Card</title>
<link href="https://fonts.googleapis.com/css2?family=Oswald:wght@400;600&family=Roboto:ital,wght@0,400;1,400&display=swap" rel="stylesheet">
<style>
  :root {
    --stage: #1c1c1c;
    --card: #f4f4f4;
    --card-edge: #e6e6e6;
    --ink: #111111;
    --ink-soft: #555555;
    --ink-muted: #6a6a6a;
  }
  html, body {
    margin: 0;
    padding: 0;
    width: 1200px;
    height: 900px;
    overflow: hidden;
    background: var(--stage);
  }
  .canvas {
    position: relative;
    width: 1200px;
    height: 900px;
    display: flex;
    align-items: center;
    justify-content: center;
  }
  .business-card {
    position: relative;
    width: 900px;
    height: 514px;
    background: linear-gradient(135deg, #ffffff 0%, var(--card) 55%, var(--card-edge) 100%);
    box-sizing: border-box;
  }
  .holder {
    position: absolute;
    left: 62px;
    top: 58px;
  }
  .holder-name {
    margin: 0;
    font-family: "Oswald", sans-serif;
    font-weight: 600;
    font-size: 30px;
    letter-spacing: 2px;
    text-transform: uppercase;
    color: var(--ink);
    line-height: 1.1;
  }
  .holder-title {
    margin: 2px 0 0;
    font-family: "Roboto", sans-serif;
    font-style: italic;
    font-size: 24px;
    color: var(--ink-soft);
  }
  .contact {
    position: absolute;
    left: 62px;
    top: 214px;
    font-family: "Roboto", sans-serif;
    font-size: 25px;
    color: var(--ink-muted);
    line-height: 1.3;
  }
  .contact-address {
    margin: 0 0 4px 40px;
    font-style: normal;
  }
  .contact-list {
    list-style: none;
    margin: 0;
    padding: 0;
  }
  .contact-item {
    display: flex;
    align-items: center;
    gap: 8px;
  }
  .contact-icon {
    width: 30px;
    height: 22px;
    flex: none;
    fill: var(--ink);
  }
  .brand {
    position: absolute;
    right: 70px;
    bottom: 70px;
    font-family: "Oswald", sans-serif;
    font-weight: 400;
    font-size: 54px;
    letter-spacing: 1px;
    text-transform: uppercase;
    color: var(--ink);
    margin: 0;
  }
</style>
</head>
<body>
<main class="canvas">
  <section class="business-card" aria-label="Korvex Systems business card">
    <header class="holder">
      <h1 class="holder-name">Darren Holt</h1>
      <p class="holder-title">Plant Manager</p>
    </header>

    <div class="contact">
      <address class="contact-address">48 Alder Crest Road,<br>Markham Vale, ON L6T 3K2</address>
      <ul class="contact-list">
        <li class="contact-item">
          <svg class="contact-icon" viewBox="0 0 30 22" aria-hidden="true">
            <path d="M3 7c0-3 5-5 12-5s12 2 12 5l-1 2h-5l-1-3h-10l-1 3h-5z"/>
            <rect x="7" y="10" width="16" height="10" rx="2"/>
          </svg>
          <span>555.204.7186</span>
        </li>
        <li class="contact-item">
          <svg class="contact-icon" viewBox="0 0 30 22" aria-hidden="true">
            <path d="M3 3h24v16h-24z M5 5l10 8 10-8" fill="var(--ink)" stroke="var(--card)" stroke-width="1.5"/>
          </svg>
          <span>dan@korvexsystems.com</span>
        </li>
        <li class="contact-item">
          <svg class="contact-icon" viewBox="0 0 30 22" aria-hidden="true">
            <circle cx="15" cy="11" r="10"/>
            <path d="M8 9c3-1 4 2 7 1s3-4 6-2M10 16c2-2 5-1 7 0" stroke="var(--card)" stroke-width="2" fill="none"/>
          </svg>
          <span>www.korvexsystems.com</span>
        </li>
      </ul>
    </div>

    <p class="brand">Korvex Systems</p>
  </section>
</main>
</body>
</html>
```